LKND - Ledgers Kept Neatly Daily

We need a business card design for a company located in Australia - accounting / tax firm.

2 sided business card - I have attached a one-sided concept that I did in MSWord :) If anything it shows that I want a striking design - bold, fresh and less reserved than your average accounting firm's card.

Rather than having all the info on the front, maybe it could just have name and logo on front?

Want to keep colours in line with logo - orange, black and white.

Happy for full colour. Will be using a matte finish.

About Us (below)
LKND does business, and more specifically accounting and taxation differently.
People require news and other media at their fingertips so why should business figures and documents be any different?
In combination with Quilo, a cloud based accounting package, we store all receipts, tax returns and special documentation with a secure online data-storage provider and provide you with your own login. We are also interested to hear if video conferencing is something you would be interested in.
Using this technology we are able to focus more on your business and less on the data entry.

Target Market(s)

Individual mum and dad clients, and Small to Medium Business

Industry/Entity Type

Accounting

Requirements
Must have
• Must be able to edit the details at a future point in time ie - phone, address, website address, name on card and slogan.

2 sided

Standard Australian business card size
Nice to have
• Rather than having all the info on the front, maybe it could just have name and logo on front?
Should not have
• Don't want "Ledgers Kept Neatly Daily" on the card

```html
<!DOCTYPE html>
<html lang="en">
<head>
<meta charset="utf-8">
<title>LKND Business Card</title>
<link rel="stylesheet" href="https://fonts.googleapis.com/css2?family=Share+Tech&family=Teko:wght@400;500&display=swap">
<style>
  :root {
    --backdrop: #eeeeec;
    --orange-light: #f9a23a;
    --orange-mid: #f2853b;
    --orange-deep: #e85a26;
    --ink: #111111;
    --card-black: #000000;
    --accent: #f7902f;
    --paper-white: #ffffff;
    --disc: #f6b04a;
  }
  * { margin: 0; padding: 0; box-sizing: border-box; }
  html, body { width: 1200px; height: 720px; overflow: hidden; }
  body {
    background: var(--backdrop);
    font-family: "Share Tech", sans-serif;
    position: relative;
  }
  .card {
    position: absolute;
    top: 97px;
    width: 300px;
    height: 525px;
    display: flex;
    flex-direction: column;
    align-items: center;
    text-transform: uppercase;
  }
  .card--front {
    left: 255px;
    background:
      radial-gradient(circle at 42% 34%, var(--orange-light) 0%, var(--orange-mid) 45%, var(--orange-deep) 100%);
  }
  .card--back {
    left: 645px;
    background: var(--card-black);
  }
  .brand-disc {
    width: 164px;
    height: 164px;
    border-radius: 50%;
    background: var(--disc);
    margin-top: 172px;
  }
  .brand-name {
    font-family: "Teko", sans-serif;
    font-weight: 400;
    font-size: 64px;
    letter-spacing: 6px;
    line-height: 1;
    color: var(--ink);
    margin-top: 44px;
  }
  .services {
    list-style: none;
    text-align: center;
    color: var(--ink);
    font-size: 11.5px;
    letter-spacing: 0.6px;
    line-height: 17px;
    margin-top: 6px;
  }
  .holder-name {
    font-family: "Teko", sans-serif;
    font-weight: 500;
    font-size: 32px;
    letter-spacing: 1.5px;
    line-height: 1;
    color: var(--accent);
    margin-top: 192px;
  }
  .holder-role {
    font-size: 12.5px;
    letter-spacing: 0.8px;
    color: var(--paper-white);
    margin-top: 2px;
  }
  .contact {
    list-style: none;
    text-align: center;
    color: var(--paper-white);
    font-size: 13px;
    letter-spacing: 0.8px;
    line-height: 18.5px;
    margin-top: 22px;
  }
</style>
</head>
<body>
  <section class="card card--front" aria-label="Card front">
    <div class="brand-disc" aria-hidden="true"></div>
    <h1 class="brand-name">LKND</h1>
    <ul class="services">
      <li>Book Keeping</li>
      <li>Accounting</li>
      <li>Taxation</li>
    </ul>
  </section>

  <section class="card card--back" aria-label="Card back">
    <h2 class="holder-name">Martin Hale</h2>
    <p class="holder-role">Tax Agent</p>
    <ul class="contact">
      <li>hale@lknd.com.au</li>
      <li>0412 555 038</li>
      <li>www.lknd.com.au</li>
    </ul>
  </section>
</body>
</html>
```